Zielgruppe
Ich bin Autorin und möchte gerne für einen Liebesroman - Zielgruppe Frauen von 20-40 Jahren - ein up-to-date Buchcover erstellt bekommen. In dem Roman geht es um Liebeskummer und darum sich selbst zu finden.
Aufgabenstellung
Der Stil sollte angelehnt sein an die Buchcover 'Zwischen zwei Gewittern' von Tilda Brannock, `Gefangen im Sommerregen` von Heike Osterwald, oder 'Wo die Möwen schlafen' von Daniela Kupfer. Detailreichtum, jung, etwas frech oder verspielt.
Titel: Herzschmerz extra - gründlich danebengegangen
Klappentext zur Orientierung:
Die Liebesgeschichte, die man zu Ende bringt, ist selten die, die man beginnt.
Claras Liebeskummer ist hausgemacht. Nein, sie kann sich ihr Leben ohne Benedikt nicht vorstellen. Und ja, ihre Versuche, ihn zurückzuerobern, sind zum Scheitern verurteilt, wenn sie sich nicht in die beste Version ihrer selbst verwandelt. Blöd nur, dass ihr hierfür nur zwölf Wochen Zeit bleiben. Da gibt es nur eine Lösung: Clara verschreibt sich mit Hilfe von Doktor Quibble eine Affäre in der Mainmetropole Frankfurt auf Rezept. Wie soll Benedikt da noch widerstehen können?

```html
<!DOCTYPE html>
<html lang="de">
<head>
<meta charset="utf-8">
<title>Herzschmerz extra – gründlich danebengegangen · Buchumschlag</title>
<link rel="stylesheet" href="https://fonts.googleapis.com/css2?family=Jost:wght@400;500;600;700;800&display=swap">
<style>
  :root {
    --page-bg: #ffffff;
    --night: #1e1936;
    --night-deep: #15102a;
    --plum: #3b1e44;
    --rose-soft: #ecabc2;
    --spark-pink: #e0457f;
    --spark-warm: #fff3d6;
    --photo-light: #f6eef2;
    --photo-pink: #c66f93;
    --photo-mauve: #9b6b8e;
    --photo-knit: #8f8aa4;
    --ink: #141014;
    --white: #ffffff;
    --cross: #b5597d;
  }
  * { box-sizing: border-box; margin: 0; padding: 0; }
  html, body { width: 849px; height: 1200px; overflow: hidden; background: var(--page-bg); }
  body { position: relative; font-family: "Jost", sans-serif; }

  .filter-defs { position: absolute; width: 0; height: 0; }

  .cover-spread {
    position: absolute; left: 0; top: 0;
    width: 849px; height: 575px;
    display: flex;
  }

  .bokeh { position: absolute; inset: 0; width: 100%; height: 100%; pointer-events: none; }

  /* Rückseite */
  .back-cover {
    position: relative; width: 413px; height: 100%;
    background:
      radial-gradient(circle at 85% 78%, rgba(190,70,120,.32), transparent 42%),
      radial-gradient(circle at 92% 30%, rgba(120,110,170,.25), transparent 30%),
      linear-gradient(165deg, var(--night) 0%, var(--night-deep) 50%, var(--plum) 100%);
    color: var(--white);
    text-align: center;
    overflow: hidden;
  }
  .back-cover .tagline {
    position: absolute; left: 30px; right: 30px; top: 120px;
    color: var(--rose-soft); font-size: 15px; font-weight: 500; line-height: 1.38;
  }
  .back-cover .blurb {
    position: absolute; left: 48px; right: 48px; top: 181px;
    font-size: 15px; font-weight: 500; line-height: 1.36;
    text-shadow: 0 0 6px rgba(0,0,0,.5);
  }

  .author-rule {
    position: absolute; left: 30px; right: 30px; top: 541px;
    display: flex; align-items: center; gap: 10px;
    color: var(--white); font-size: 13.5px; font-weight: 500; letter-spacing: .03em;
  }
  .author-rule::before, .author-rule::after {
    content: ""; flex: 1; height: 1.5px; background: var(--white);
  }

  /* Buchrücken */
  .spine {
    position: relative; width: 31px; height: 100%;
    background: linear-gradient(180deg, var(--night-deep), var(--night) 55%, var(--plum));
    color: var(--white);
    overflow: hidden;
  }
  .spine .spine-text {
    position: absolute; left: 50%;
    transform: translate(-50%, -50%) rotate(-90deg);
    white-space: nowrap; font-size: 11px; font-weight: 500; letter-spacing: .05em;
  }
  .spine .spine-author { top: 89px; }
  .spine .spine-title { top: 378px; }

  /* Vorderseite */
  .front-cover {
    position: relative; width: 405px; height: 100%;
    overflow: hidden;
  }
  .front-photo {
    position: absolute; inset: 0;
    background:
      radial-gradient(ellipse 40% 30% at 38% 20%, rgba(255,255,255,.85), transparent 70%),
      radial-gradient(ellipse 55% 40% at 15% 55%, rgba(250,240,245,.8), transparent 70%),
      radial-gradient(ellipse 50% 45% at 90% 40%, var(--photo-pink), transparent 75%),
      radial-gradient(ellipse 60% 35% at 30% 92%, var(--photo-knit), transparent 75%),
      radial-gradient(ellipse 45% 40% at 92% 88%, var(--photo-pink), transparent 75%),
      linear-gradient(175deg, var(--photo-mauve) 0%, #d5a3b8 35%, #c88ea8 65%, var(--photo-mauve) 100%);
  }
  .front-title {
    position: absolute; left: 0; right: 0; top: 262px;
    text-align: center; color: var(--ink);
    font-weight: 700; text-transform: uppercase;
  }
  .front-title .distressed { filter: url(#distress); display: block; }
  .front-title .line-main { font-size: 40px; letter-spacing: .06em; line-height: 1.1; }
  .front-title .plus { display: block; margin: 4px auto 8px; width: 74px; height: 74px; }
  .front-title .line-sub { font-size: 31px; letter-spacing: .05em; line-height: 1.12; }
</style>
</head>
<body>
  <svg class="filter-defs" aria-hidden="true">
    <defs>
      <filter id="distress" x="0" y="0" width="100%" height="100%">
        <feTurbulence type="fractalNoise" baseFrequency="0.85" numOctaves="2" seed="4" result="noise"/>
        <feColorMatrix in="noise" type="matrix" values="0 0 0 0 0  0 0 0 0 0  0 0 0 0 0  -3 0 0 0 2.3" result="mask"/>
        <feComposite in="SourceGraphic" in2="mask" operator="in"/>
      </filter>
      <filter id="soft" x="-50%" y="-50%" width="200%" height="200%">
        <feGaussianBlur stdDeviation="1.2"/>
      </filter>
    </defs>
  </svg>

  <div class="cover-spread">
    <section class="back-cover">
      <svg class="bokeh" viewBox="0 0 413 575" aria-hidden="true">
        <g filter="url(#soft)">
          <circle cx="60" cy="125" r="14" fill="#6d7fa8" opacity=".18"/>
          <circle cx="150" cy="110" r="18" fill="#6d7fa8" opacity=".14"/>
          <circle cx="355" cy="180" r="16" fill="#6d7fa8" opacity=".15"/>
          <circle cx="385" cy="225" r="3" fill="var(--spark-warm)" opacity=".9"/>
          <circle cx="395" cy="260" r="5" fill="var(--spark-warm)" opacity=".85"/>
          <circle cx="360" cy="275" r="2.5" fill="var(--spark-warm)" opacity=".9"/>
          <circle cx="378" cy="300" r="2" fill="var(--white)" opacity=".9"/>
          <circle cx="400" cy="320" r="2.5" fill="var(--white)" opacity=".7"/>
          <circle cx="355" cy="345" r="6" fill="#b58ab8" opacity=".35"/>
          <circle cx="390" cy="365" r="3" fill="var(--spark-pink)" opacity=".8"/>
          <circle cx="345" cy="395" r="4" fill="var(--spark-pink)" opacity=".7"/>
          <circle cx="372" cy="415" r="2.5" fill="var(--spark-pink)" opacity=".9"/>
          <circle cx="310" cy="430" r="3" fill="var(--spark-pink)" opacity=".6"/>
          <circle cx="398" cy="440" r="5" fill="var(--spark-pink)" opacity=".65"/>
          <circle cx="330" cy="465" r="2.5" fill="var(--spark-pink)" opacity=".8"/>
          <circle cx="365" cy="478" r="4" fill="var(--spark-pink)" opacity=".55"/>
          <circle cx="285" cy="470" r="2" fill="var(--spark-pink)" opacity=".7"/>
          <circle cx="395" cy="500" r="3" fill="var(--spark-pink)" opacity=".6"/>
          <circle cx="250" cy="495" r="2.5" fill="var(--spark-pink)" opacity=".45"/>
          <circle cx="340" cy="510" r="2" fill="var(--spark-pink)" opacity=".6"/>
        </g>
      </svg>
      <p class="tagline">Die Liebesgeschichte, die man zu Ende bringt,<br>ist selten die, die man beginnt.</p>
      <p class="blurb">Claras Liebeskummer ist hausgemacht. Nein, sie kann sich ihr Leben ohne Benedikt nicht vorstellen. Und ja, ihre Versuche, ihn zurückzuerobern, sind zum Scheitern verurteilt, wenn sie sich nicht in die beste Version ihrer selbst verwandelt. Blöd nur, dass ihr hierfür nur zwölf Wochen Zeit bleiben. Da gibt es nur eine Lösung: Clara verschreibt sich mit Hilfe von Doktor Quibble eine Affäre in der Mainmetropole Frankfurt auf Rezept. Wie soll Benedikt da noch widerstehen können?</p>
      <div class="author-rule">QUELLY AUTORNAME</div>
    </section>

    <section class="spine">
      <svg class="bokeh" viewBox="0 0 31 575" aria-hidden="true">
        <circle cx="8" cy="250" r="2" fill="var(--spark-warm)" opacity=".8"/>
        <circle cx="20" cy="300" r="1.5" fill="var(--white)" opacity=".8"/>
        <circle cx="6" cy="420" r="2" fill="var(--spark-pink)" opacity=".7"/>
        <circle cx="24" cy="470" r="2" fill="var(--spark-pink)" opacity=".6"/>
      </svg>
      <span class="spine-text spine-author">QUELLY AUTORNAME</span>
      <span class="spine-text spine-title">HERZSCHMERZ + GRÜNDLICH DANEBENGEGANGEN</span>
    </section>

    <section class="front-cover">
      <div class="front-photo" role="img" aria-label="Foto: ein Paar kurz vor dem Kuss in rosa-violettem Licht, sie im grauen Strickpullover"></div>
      <svg class="bokeh" viewBox="0 0 405 575" aria-hidden="true">
        <g filter="url(#soft)">
          <circle cx="20" cy="440" r="2" fill="var(--white)" opacity=".8"/>
          <circle cx="45" cy="470" r="3" fill="var(--spark-pink)" opacity=".6"/>
          <circle cx="80" cy="455" r="2" fill="var(--white)" opacity=".7"/>
          <circle cx="110" cy="480" r="4" fill="var(--spark-pink)" opacity=".55"/>
          <circle cx="150" cy="500" r="2.5" fill="var(--white)" opacity=".7"/>
          <circle cx="190" cy="470" r="3" fill="var(--spark-pink)" opacity=".6"/>
          <circle cx="207" cy="492" r="4" fill="var(--white)" opacity=".9"/>
          <circle cx="235" cy="505" r="5" fill="var(--spark-pink)" opacity=".55"/>
          <circle cx="260" cy="520" r="3" fill="var(--spark-pink)" opacity=".6"/>
          <circle cx="285" cy="500" r="2" fill="var(--white)" opacity=".6"/>
          <circle cx="215" cy="530" r="2.5" fill="var(--spark-pink)" opacity=".7"/>
          <circle cx="120" cy="520" r="2" fill="var(--spark-pink)" opacity=".6"/>
          <circle cx="60" cy="510" r="3" fill="var(--white)" opacity=".5"/>
          <circle cx="300" cy="470" r="2" fill="var(--spark-pink)" opacity=".5"/>
          <circle cx="10" cy="350" r="2" fill="var(--white)" opacity=".7"/>
          <circle cx="30" cy="300" r="1.5" fill="var(--white)" opacity=".6"/>
        </g>
      </svg>
      <h1 class="front-title">
        <span class="distressed line-main">Herzschmerz</span>
        <svg class="plus" viewBox="0 0 74 74" aria-label="plus">
          <rect x="28" y="0" width="18" height="74" fill="var(--cross)"/>
          <rect x="0" y="28" width="74" height="18" fill="var(--cross)"/>
        </svg>
        <span class="distressed line-sub">Gründlich<br>danebengegangen</span>
      </h1>
      <div class="author-rule">QUELLY AUTORNAME</div>
    </section>
  </div>
</body>
</html>
```